Refer a Friend A5 Flyer for Healthcare Staff

We need an A5 flyer that we can hand out to existing and new staff members promoting our Refer a friend Scheme. We need the leaflet to encourage staff to talk to their family and friends about joining our Healthcare Agency, which provides staff to local care related establishments. Using our logo and brand colours blue and green, as per our website, the final design will need to clearly convey the benefits and attractions of referring additional staff to the team. In addition is the promotion of our Circlepage page, requesting staff to like the page and to like and share various posts.

Target Market(s)

Healthcare and potential Healthcare Staff

Industry/Entity Type

Healthcare

Colors
33b8a4
3277b5

Requirements
Must have
• Company Logo, Brand colours,
• text; "Refer a Friend and receive a £50 Bonus after just 1 completed shift"
• text; "3 easy steps to refer a friend, 1 Fill out your name on the back of your Business Card 2 Hand the card to your friend or any person you wish to refer, 3 ask your friend to present the card to us when they attend their interview"
• text; "Like and share any of our Open Days on Circlepage for a chance to win a prize, you can find us easily by searching @CarewellPlacementGroup"
• text; "Like our Page to stay up to date with our events and offers"
Nice to have
• care worker / elderly care / support worker pictures
• Content / pics from website www.carewellplacementgroup.co.uk

```html
<!DOCTYPE html>
<html lang="en">
<head>
<meta charset="utf-8">
<title>Carewell Placement Group – Refer a Friend Flyer</title>
<link rel="stylesheet" href="https://fonts.googleapis.com/css2?family=Montserrat:wght@800&family=Open+Sans:wght@400;600;700&display=swap">
<style>
  :root {
    --brand-navy: #2b4a9c;
    --headline-green: #2bb197;
    --body-grey: #5b5b5b;
    --rule-blue: #3f5fa8;
    --paper: #ffffff;
  }
  * { margin: 0; padding: 0; box-sizing: border-box; }
  html, body {
    width: 856px; height: 1200px; overflow: hidden;
    background: var(--paper);
  }
  .flyer {
    position: relative; width: 856px; height: 1200px; overflow: hidden;
    background: var(--paper);
    font-family: "Open Sans", Arial, sans-serif;
  }
  .visual-panel {
    position: absolute; left: 462px; top: 0; width: 394px; height: 1200px;
  }
  .frame-lines {
    position: absolute; left: 0; top: 0; width: 856px; height: 1200px;
    pointer-events: none;
  }
  .content {
    position: absolute; left: 44px; top: 0; width: 400px; height: 1200px;
  }
  .brand {
    position: absolute; top: 74px; left: 0;
    display: flex; align-items: center; gap: 14px;
    color: var(--brand-navy);
  }
  .brand-mark {
    flex: none; width: 24px; height: 24px; border-radius: 50%;
    background: var(--brand-navy);
  }
  .brand-name {
    font-weight: 400; font-size: 36px; line-height: 42px; letter-spacing: -0.5px;
  }
  .headline {
    position: absolute; top: 214px; left: 0; width: 400px;
    font-family: "Montserrat", Arial, sans-serif; font-weight: 800;
    color: var(--headline-green); text-transform: uppercase;
    font-size: 37px; letter-spacing: -0.2px;
  }
  .headline span { display: block; white-space: nowrap; }
  .headline .l1 { line-height: 44px; }
  .headline .l2 { line-height: 46px; }
  .headline .bonus { color: var(--brand-navy); font-size: 57px; line-height: 50px; }
  .headline .l4 { line-height: 44px; }
  .headline .l5 { line-height: 38px; }
  .rule {
    position: absolute; left: 0; width: 394px; height: 0;
    border-top: 1.5px solid var(--rule-blue);
  }
  .rule.one { top: 464px; }
  .rule.two { top: 855px; }
  .rule.three { top: 1062px; }
  .steps-title {
    position: absolute; top: 490px; left: 0; width: 394px;
    color: var(--brand-navy); font-weight: 600;
    font-size: 34px; line-height: 41px; letter-spacing: -0.4px;
  }
  .steps {
    position: absolute; top: 577px; left: 0; width: 400px;
    list-style: none; color: var(--body-grey);
    font-weight: 700; font-size: 20px; line-height: 28px;
  }
  .steps li { position: relative; padding-left: 16px; white-space: nowrap; }
  .steps li + li { margin-top: 27px; }
  .steps li::before {
    content: ""; position: absolute; left: 0; top: 12px;
    width: 5px; height: 5px; border-radius: 50%; background: var(--brand-navy);
  }
  .social-note {
    position: absolute; top: 880px; left: 0; width: 400px;
    color: var(--body-grey); font-size: 22px; line-height: 29px; white-space: nowrap;
  }
  .handle {
    position: absolute; top: 993px; left: 0;
    color: var(--brand-navy); font-weight: 700; font-size: 28px; letter-spacing: -0.3px;
  }
  .page-note {
    position: absolute; top: 1090px; left: 0; width: 400px;
    color: var(--body-grey); font-size: 22px; line-height: 30px;
  }
  .page-note strong {
    display: block; color: var(--brand-navy); font-weight: 700; font-size: 29px; line-height: 40px;
  }
</style>
</head>
<body>
<main class="flyer">

  <svg class="visual-panel" viewBox="0 0 394 1200" xmlns="http://www.w3.org/2000/svg">
    <defs>
      <linearGradient id="tealBg" x1="0" y1="0" x2="1" y2="1">
        <stop offset="0" stop-color="#1fa891"/>
        <stop offset="0.5" stop-color="#33b8a4"/>
        <stop offset="1" stop-color="#1a9d89"/>
      </linearGradient>
      <linearGradient id="careRoom" x1="0" y1="0" x2="1" y2="1">
        <stop offset="0" stop-color="#c9b68e"/>
        <stop offset="0.6" stop-color="#9c7d5f"/>
        <stop offset="1" stop-color="#6b4e3f"/>
      </linearGradient>
      <linearGradient id="walkingFrame" x1="0" y1="0" x2="1" y2="1">
        <stop offset="0" stop-color="#d8cfc4"/>
        <stop offset="0.5" stop-color="#8e4a5a"/>
        <stop offset="1" stop-color="#5c2a38"/>
      </linearGradient>
      <linearGradient id="nurseHug" x1="0" y1="0" x2="1" y2="1">
        <stop offset="0" stop-color="#e0d6cc"/>
        <stop offset="0.5" stop-color="#c8713c"/>
        <stop offset="1" stop-color="#5a93c8"/>
      </linearGradient>
    </defs>
    <rect width="394" height="1200" fill="url(#tealBg)"/>
    <polygon points="120,130 320,330 120,530 -80,330" fill="none" stroke="#ffffff" stroke-opacity="0.25" stroke-width="1.5"/>
    <polygon points="300,60 420,180 300,300 180,180" fill="none" stroke="#2b4a9c" stroke-width="1.5"/>
    <polygon points="280,720 420,860 280,1000 140,860" fill="none" stroke="#2b4a9c" stroke-opacity="0.8" stroke-width="1.5"/>
    <polygon points="120,1020 240,1140 120,1260 0,1140" fill="none" stroke="#ffffff" stroke-opacity="0.3" stroke-width="1.5"/>

    <g role="img" aria-label="Photo: carer holding the hand of an elderly man in a wheelchair by a window">
      <polygon points="163,85 340,262 163,439 -14,262" fill="url(#careRoom)" stroke="#ffffff" stroke-width="2"/>
    </g>
    <g role="img" aria-label="Photo: care worker supporting an elderly woman using a walking frame">
      <polygon points="176,336 438,598 176,860 -86,598" fill="url(#walkingFrame)" stroke="#ffffff" stroke-width="2"/>
    </g>
    <g role="img" aria-label="Photo: smiling nurse embracing an elderly woman">
      <polygon points="183,760 364,941 183,1122 2,941" fill="url(#nurseHug)" stroke="#ffffff" stroke-width="2"/>
    </g>
  </svg>

  <svg class="frame-lines" viewBox="0 0 856 1200" xmlns="http://www.w3.org/2000/svg" aria-hidden="true">
    <polygon points="405,-80 515,30 405,140 295,30" fill="none" stroke="#2b4a9c" stroke-width="1.5"/>
    <polygon points="387,112 405,130 387,148 369,130" fill="none" stroke="#2b4a9c" stroke-width="1.5"/>
    <polygon points="470,1100 560,1190 470,1280 380,1190" fill="none" stroke="#2b4a9c" stroke-width="1.5"/>
  </svg>

  <section class="content">
    <div class="brand">
      <span class="brand-mark"></span>
      <span class="brand-name">Carewell<br>Placement Group</span>
    </div>

    <h1 class="headline">
      <span class="l1">Refer a friend</span>
      <span class="l2">and receive a</span>
      <span class="bonus">£50 Bonus</span>
      <span class="l4">after just 1</span>
      <span class="l5">completed shift</span>
    </h1>

    <div class="rule one"></div>

    <h2 class="steps-title">3 easy steps to refer a<br>friend...</h2>
    <ul class="steps">
      <li>Fill out your name on the back of<br>your Business Card</li>
      <li>Hand the card to your friend or any<br>person you wish to refer</li>
      <li>Ask your friend to present the card<br>to us when they attend their<br>interview</li>
    </ul>

    <div class="rule two"></div>

    <p class="social-note">Like and share any of our Open Days<br>on Circlepage for a chance to win a<br>prize, you can find us easily<br>by searching</p>
    <p class="handle">@CarewellPlacementGroup</p>

    <div class="rule three"></div>

    <p class="page-note">Like our Page to stay up to date with <strong>our events and offers</strong></p>
  </section>

</main>
</body>
</html>
```